website design for a new age Real Estate Security Business

We are launching a business in real estate which no body else is doing. We are going to use technology in terms of software and hardware to provide our services.

We are going to use Big Data, IOT etc.. for our services.

NOTE: We don't want to see Shiel or buildings etc.. that directly suggests Real estate or security on this design

Target Market(s)

India

Industry/Entity Type

Real Estate

Number of Pages Required

4 page

Font styles to use
Sans Serif
Other font styles liked:
• Use Google Fonts

Requirements
Must have
• Home Page should be trendy and colourful should give user confidence to subscribe to our service.
Nice to have
• Use Google fonts.
Should not have
• Design shouldnt have Shield or Buildings that directly suggests real estate or security.

```html
<!DOCTYPE html>
<html lang="en">
<head>
<meta charset="utf-8">
<title>Parcel Warden — Data, Analysis, Action</title>
<link href="https://fonts.googleapis.com/css2?family=Montserrat:wght@300;400;500;600;700&family=Bebas+Neue&family=Tinos&display=swap" rel="stylesheet">
<style>
:root{
  --green:#2db55d;
  --green-dark:#1f9a4a;
  --ink:#1d1d1d;
  --muted:#6b6b6b;
  --navy:#1b3352;
  --blue:#4a9be6;
  --lavender:#e9ecfd;
  --list-blue:#cfe3fb;
  --red:#f4543a;
  --teal:#22dde0;
  --gold:#ffb100;
  --white:#ffffff;
}
*{margin:0;padding:0;box-sizing:border-box}
html,body{width:1200px;height:3226px;overflow:hidden}
body{font-family:"Montserrat",sans-serif;color:var(--ink);background:var(--white);position:relative}
.abs{position:absolute}

/* header */
.topbar{left:0;top:0;width:1200px;height:75px;background:#f7f7f7;border-bottom:3px solid var(--green)}
.brand{left:88px;top:6px;width:148px;height:166px;background:#6aa3e0;border:4px solid var(--white);box-shadow:0 2px 6px rgba(0,0,0,.25);display:flex;flex-direction:column;align-items:center;justify-content:center;z-index:5}
.brand span{font-family:"Montserrat",sans-serif;font-weight:700;font-size:19px;color:var(--white);line-height:1.2;text-align:center}
.nav{left:343px;top:0;height:75px;display:flex;align-items:center;gap:0;font-family:"Tinos",serif;font-size:17px;color:#222}
.nav a{color:inherit;text-decoration:none;display:block;margin-right:64px;position:relative;height:75px;line-height:75px}
.nav a.active{color:var(--blue)}
.nav a.active::after{content:"";position:absolute;left:-6px;right:-6px;bottom:0;height:4px;background:var(--blue)}
.nav .cart{margin-right:0}

/* hero */
.hero{left:0;top:75px;width:1200px;height:340px;background:radial-gradient(ellipse at 50% 45%,#0c3b5a 0%,#06192a 45%,#000 80%)}
.hero-title{left:0;top:190px;width:1200px;text-align:center;font-family:"Bebas Neue",sans-serif;font-size:46px;color:var(--white);letter-spacing:1px;display:flex;justify-content:center;gap:26px;align-items:center}
.hero-title span{display:flex;align-items:center;gap:8px}
.hero-sub{left:0;top:252px;width:1200px;text-align:center;font-family:"Tinos",serif;font-size:24px;color:#6fe07a;letter-spacing:.5px}

/* section headings */
.sec-title{left:0;width:1200px;text-align:center;font-weight:700;font-size:31px}
.sec-title em{font-style:normal;color:var(--green)}
.sec-sub{left:0;width:1200px;text-align:center;font-size:15px;color:var(--muted)}
.divider{left:466px;width:268px;height:1px;background:#ddd}
.divider::after{content:"";position:absolute;left:109px;top:-2px;width:50px;height:4px;background:var(--green)}
.about-copy{left:130px;top:600px;width:940px;text-align:center;font-size:13px;line-height:22px;color:#444}

/* feature rows */
.feature-doc{left:0;top:727px;width:1200px;height:537px;background:var(--lavender)}
.img-doc{left:30px;top:40px;width:590px;height:460px;background:radial-gradient(ellipse at 40% 50%,#f2dd8a 0%,#e3c868 35%,#b9c5e8 70%,var(--lavender) 100%);border-radius:8px}
.feat-title{font-size:28px;font-weight:400}
.feat-copy{font-size:14px;line-height:24px;color:#555}
.btn-outline{border:2px solid #9fd9b4;border-radius:4px;font-size:15px;font-weight:600;color:var(--green);padding:9px 16px;background:transparent}
.img-land{left:658px;top:1264px;width:542px;height:559px;background:radial-gradient(ellipse at 55% 55%,#3e9bea 0%,#7fbff2 35%,#b8d9f8 65%,#e3effc 100%)}
.ticks{display:flex;gap:28px;font-size:13px;font-weight:600;color:#333}
.ticks span{display:flex;align-items:center;gap:6px}

/* pricing */
.card{top:2017px;width:323px;height:535px}
.card-head{height:47px;line-height:47px;text-align:center;color:var(--white);font-size:22px;font-weight:500}
.card-price{height:161px;background:var(--green);color:var(--white);display:flex;align-items:center;justify-content:center;gap:4px}
.card-price sup{font-size:18px;align-self:flex-start;margin-top:52px}
.card-price b{font-weight:300;font-size:58px}
.card-price small{font-size:12px;align-self:flex-end;margin-bottom:58px}
.card-body{height:280px;background:var(--list-blue);padding:36px 22px 0}
.card-body ul{list-style:none;margin-left:86px}
.card-body li{font-size:16px;font-weight:500;height:41px;display:flex;align-items:center;gap:10px}
.card-body p{font-size:13px;line-height:26px;text-align:center;color:#666;margin-top:22px}
.card-foot{height:47px;line-height:47px;text-align:center;color:var(--white);font-size:21px;font-weight:600}

/* newsletter */
.news{left:0;top:2612px;width:1200px;height:93px;background:var(--white);border-top:1px solid #cfd8e3}
.news-band{left:0;top:2612px;width:520px;height:93px;background:var(--blue);clip-path:polygon(0 0,100% 0,96% 100%,0 100%)}
.news-band h2{position:absolute;left:86px;top:28px;font-size:30px;font-weight:600;color:var(--white)}
.news-input{left:555px;top:2634px;width:420px;height:50px;border:1px solid #b8c6d6;border-right:none;font-size:12px;color:#666;padding-left:16px;line-height:48px}
.news-btn{left:975px;top:2634px;width:137px;height:50px;background:var(--blue);color:var(--white);font-size:18px;font-weight:500;text-align:center;line-height:50px;border-radius:0 4px 4px 0}

/* contact */
.contact-bg{left:0;top:2705px;width:1200px;height:455px;background:linear-gradient(90deg,#d9d6d3 0%,#c9cdd2 30%,#6f9b7c 55%,#d7b89c 100%)}
.touch{left:86px;top:2705px;width:460px;height:455px;background:rgba(255,255,255,.9);text-align:center}
.touch h3{margin-top:86px;font-size:25px;font-weight:700;color:#1b3f7a}
.touch p{font-size:14px;line-height:22px;color:#333}
.touch .ico{margin:20px auto 6px;display:block}
.form{left:546px;top:2705px;width:568px;height:455px;background:rgba(45,181,93,.9);color:var(--white)}
.form h3{position:absolute;left:0;width:568px;top:86px;text-align:center;font-size:25px;font-weight:600}
.form h3::after{content:"";position:absolute;left:260px;top:44px;width:48px;height:2px;background:rgba(255,255,255,.8)}
.field{position:absolute;left:38px;width:460px;height:46px;border:1px solid rgba(255,255,255,.75);font-size:12px;padding:12px 14px;color:rgba(255,255,255,.9)}
.form .submit{position:absolute;left:392px;top:320px;width:138px;height:44px;border:1px solid rgba(255,255,255,.8);border-radius:4px;font-size:19px;font-weight:600;text-align:center;line-height:42px}

/* footer */
.footer{left:0;top:3160px;width:1200px;height:66px;background:var(--navy)}
.footer p{position:absolute;left:86px;top:25px;font-size:13px;color:#7f93ab}
.socials{position:absolute;left:910px;top:14px;display:flex;gap:18px}
.socials i{display:block;width:30px;height:30px;border:1px solid #8fa2b8;transform:rotate(45deg);margin:4px 2px}
</style>
</head>
<body>

<header>
  <div class="abs topbar"></div>
  <div class="abs brand"><span>Parcel<br>Warden</span></div>
  <nav class="abs nav">
    <a class="active">Home</a>
    <a>About us</a>
    <a>Services</a>
    <a>Contact</a>
    <a>Pricing</a>
    <a><svg width="16" height="16" viewBox="0 0 16 16"><circle cx="6.5" cy="6.5" r="5" fill="none" stroke="#222" stroke-width="2"/><path d="M10 10l5 5" stroke="#222" stroke-width="2.4"/></svg></a>
    <a class="cart"><svg width="16" height="14" viewBox="0 0 16 14"><path d="M0 1h3l2 8h9l2-6H4" fill="none" stroke="#222" stroke-width="1.8"/><circle cx="6" cy="12" r="1.5" fill="#222"/><circle cx="13" cy="12" r="1.5" fill="#222"/></svg> 0 Items</a>
  </nav>
</header>

<section>
  <div class="abs hero" role="img" aria-label="Dark blue digital data cityscape glowing with points of light"></div>
  <h1 class="abs hero-title">
    <span><svg width="30" height="30" viewBox="0 0 30 30"><path d="M4 15h20M16 6l9 9-9 9" fill="none" stroke="#fff" stroke-width="3.5"/><path d="M2 4l6 0M2 26l6 0" stroke="#fff" stroke-width="3"/></svg>Data</span>
    <span><svg width="30" height="30" viewBox="0 0 30 30"><path d="M4 15h20M16 6l9 9-9 9" fill="none" stroke="#fff" stroke-width="3.5"/><path d="M2 4l6 0M2 26l6 0" stroke="#fff" stroke-width="3"/></svg>Analysis</span>
    <span><svg width="30" height="30" viewBox="0 0 30 30"><path d="M4 15h20M16 6l9 9-9 9" fill="none" stroke="#fff" stroke-width="3.5"/><path d="M2 4l6 0M2 26l6 0" stroke="#fff" stroke-width="3"/></svg>Action</span>
  </h1>
  <p class="abs hero-sub">TO KEEP YOUR PROPERTY SAFE</p>
</section>

<section>
  <h2 class="abs sec-title" style="top:470px">About <em>Parcel Warden</em></h2>
  <p class="abs sec-sub" style="top:520px">Nemo enim ipsam voluptatem quia voluptas aspernatur</p>
  <div class="abs divider" style="top:570px"></div>
  <p class="abs about-copy">Lorem Ipsum is simply dummy text of the printing and typesetting industry. Lorem Ipsum has been the industry's standard dummy text ever since the 1500s, when an unknown printer took a galley of type and scrambled it to make a type specimen book. It has survived not only five centuries</p>
</section>

<section>
  <div class="abs feature-doc">
    <div class="abs img-doc" role="img" aria-label="Yellow document folder with a large silver and blue key in its lock"></div>
    <h3 class="abs feat-title" style="left:641px;top:114px">Doc Secure</h3>
    <p class="abs feat-copy" style="left:641px;top:175px;width:480px">Lorem Ipsum is simply dummy text of the printing and typesetting industry. Lorem Ipsum has been the industry's standard dummy text ever since the 1500s, when an unknown printer took a galley of type and scrambled it to make a type specimen book. It has survived not only five centuries, but also the leap into electronic typesetting, remaining essentially unchanged. It was popularised in the</p>
    <div class="abs btn-outline" style="left:641px;top:375px">Learn More</div>
  </div>
</section>

<section>
  <h3 class="abs feat-title" style="left:86px;top:1366px;color:var(--green)">Land Secure</h3>
  <p class="abs feat-copy" style="left:86px;top:1430px;width:520px">Lorem Ipsum is simply dummy text of the printing and typesetting industry. Lorem Ipsum has been the industry's standard dummy text ever since the 1500s, when an unknown printer took a galley of type and scrambled it to make a type specimen book. It has survived not only five centuries, but also the leap into electronic typesetting, remaining essentially unchanged. It was popularised in the</p>
  <div class="abs ticks" style="left:86px;top:1612px">
    <span><svg width="14" height="14" viewBox="0 0 14 14"><circle cx="7" cy="7" r="6" fill="none" stroke="#2db55d" stroke-width="1.6"/><path d="M4 7l2 2 4-4" fill="none" stroke="#2db55d" stroke-width="1.6"/></svg>remaining essentially</span>
    <span><svg width="14" height="14" viewBox="0 0 14 14"><circle cx="7" cy="7" r="6" fill="none" stroke="#2db55d" stroke-width="1.6"/><path d="M4 7l2 2 4-4" fill="none" stroke="#2db55d" stroke-width="1.6"/></svg>unchanged.</span>
    <span><svg width="14" height="14" viewBox="0 0 14 14"><circle cx="7" cy="7" r="6" fill="none" stroke="#2db55d" stroke-width="1.6"/><path d="M4 7l2 2 4-4" fill="none" stroke="#2db55d" stroke-width="1.6"/></svg>It was popularised</span>
  </div>
  <div class="abs btn-outline" style="left:86px;top:1675px;border-color:#9cc4ee;color:#2f7fcf">Learn More</div>
  <div class="abs img-land" role="img" aria-label="Tablet on a light blue background with floating connected-home app icons"></div>
</section>

<section>
  <h2 class="abs sec-title" style="top:1880px">Our <em>Pricing</em></h2>
  <p class="abs sec-sub" style="top:1928px">Nemo enim ipsam voluptatem quia voluptas aspernatur</p>
  <div class="abs divider" style="top:1976px"></div>

  <div class="abs card" style="left:86px">
    <div class="card-head" style="background:var(--red)">Standard</div>
    <div class="card-price"><sup>$</sup><b>1,99</b><small>Per/Month</small></div>
    <div class="card-body">
      <ul style="color:var(--red)">
        <li><svg width="20" height="16" viewBox="0 0 20 16"><path d="M2 8l6 6L18 2" fill="none" stroke="#2db55d" stroke-width="3"/></svg>10 GB</li>
        <li><svg width="20" height="16" viewBox="0 0 20 16"><path d="M2 8l6 6L18 2" fill="none" stroke="#2db55d" stroke-width="3"/></svg>1 Domain</li>
        <li><svg width="20" height="16" viewBox="0 0 20 16"><path d="M2 8l6 6L18 2" fill="none" stroke="#2db55d" stroke-width="3"/></svg>4 mail</li>
      </ul>
      <p>type specimen book. It has survived not only five centuries, but also the leap into electronic typesetting</p>
    </div>
    <div class="card-foot" style="background:var(--red)">More</div>
  </div>

  <div class="abs card" style="left:437px">
    <div class="card-head" style="background:var(--teal)">Extended</div>
    <div class="card-price"><sup>$</sup><b>1,99</b><small>Per/Month</small></div>
    <div class="card-body">
      <ul style="color:#14b8c0">
        <li><svg width="20" height="16" viewBox="0 0 20 16"><path d="M2 8l6 6L18 2" fill="none" stroke="#2db55d" stroke-width="3"/></svg>10 GB</li>
        <li><svg width="20" height="16" viewBox="0 0 20 16"><path d="M2 8l6 6L18 2" fill="none" stroke="#2db55d" stroke-width="3"/></svg>1 Domain</li>
        <li><svg width="20" height="16" viewBox="0 0 20 16"><path d="M2 8l6 6L18 2" fill="none" stroke="#2db55d" stroke-width="3"/></svg>4 mail</li>
      </ul>
      <p>type specimen book. It has survived not only five centuries, but also the leap into electronic typesetting</p>
    </div>
    <div class="card-foot" style="background:var(--teal)">More</div>
  </div>

  <div class="abs card" style="left:789px">
    <div class="card-head" style="background:var(--gold)">Premium</div>
    <div class="card-price"><sup>$</sup><b>1,99</b><small>Per/Month</small></div>
    <div class="card-body">
      <ul style="color:var(--gold)">
        <li><svg width="20" height="16" viewBox="0 0 20 16"><path d="M2 8l6 6L18 2" fill="none" stroke="#2db55d" stroke-width="3"/></svg>10 GB</li>
        <li><svg width="20" height="16" viewBox="0 0 20 16"><path d="M2 8l6 6L18 2" fill="none" stroke="#2db55d" stroke-width="3"/></svg>1 Domain</li>
        <li><svg width="20" height="16" viewBox="0 0 20 16"><path d="M2 8l6 6L18 2" fill="none" stroke="#2db55d" stroke-width="3"/></svg>4 mail</li>
      </ul>
      <p>type specimen book. It has survived not only five centuries, but also the leap into electronic typesetting</p>
    </div>
    <div class="card-foot" style="background:var(--gold)">More</div>
  </div>
</section>

<section>
  <div class="abs news"></div>
  <div class="abs news-band"><h2>Subscribe Our Newsletter</h2></div>
  <div class="abs news-input">Enter your email</div>
  <div class="abs news-btn">Subscribe</div>
</section>

<section>
  <div class="abs contact-bg" role="img" aria-label="Soft-focus photo of a desk with a keyboard and papers"></div>
  <div class="abs touch">
    <h3>Get in touch</h3>
    <svg class="ico" width="22" height="22" viewBox="0 0 22 22"><path d="M2 5l6-3 6 3 6-3v15l-6 3-6-3-6 3z" fill="#2db55d"/><path d="M8 2v15M14 5v15" stroke="#fff" stroke-width="1.2"/></svg>
    <p>Lorem Ipsum is that it has a more-or-less<br>normal distribution of letters</p>
    <svg class="ico" width="20" height="20" viewBox="0 0 20 20"><path d="M4 1l4 4-2 3c1 3 3 5 6 6l3-2 4 4-3 3C8 19 1 12 1 4z" fill="#2db55d"/></svg>
    <p>Phone Number: +1-555-210-4786</p>
    <svg class="ico" width="22" height="22" viewBox="0 0 22 22"><circle cx="11" cy="11" r="10" fill="#2db55d"/><rect x="5" y="7" width="12" height="8" fill="#fff"/><path d="M5 7l6 5 6-5" fill="none" stroke="#2db55d" stroke-width="1.2"/></svg>
    <p>Email: hello@parcelwarden-mail.com</p>
  </div>
  <div class="abs form">
    <h3>Contact Us</h3>
    <div class="field" style="top:157px">Your Name</div>
    <div class="field" style="top:215px">Your Email</div>
    <div class="field" style="top:273px;width:254px;height:88px">Your Comments</div>
    <div class="submit">Submit</div>
  </div>
</section>

<footer class="abs footer">
  <p>2017 © ParcelWarden. All Rights Reserved.</p>
  <div class="socials"><i></i><i></i><i></i><i></i></div>
</footer>

</body>
</html>
```